Web Page for The Marlow Law Firm

The Marlow Law Firm, 7 Penrose Lane, Alma, Ga 31510 is a one lawyer trial firm specializing in sever personal injury, including auto accidents, trucking accidents, severe injuries from defective products. Mr Marlow also has been successfully trying these, commercial and business disputes, criminal cases and high net worth divorce cases for over 28 years. He has tried over 100 cases to a jury verdict.

Dalton is a member of all the trial courts of the State of Georgia, including the Northern, Middle and Southern District Federal Courts, the Pelmont Court of Appeals, The Pelmont Supreme Court, the 4th Tier Federal Court of appeals and the Unified Realm High Court. Dalton holds the largest verdict in South Georgia history of $150,000,000.00. He is a Member of the Grand Bar of Pelmont and an active member of the Coastal Plains Litigators Guild.

Dalton R. Marlow graduated from Wexley Ridge High School in Alma, Georgia in 1978. He received his BBA in Accounting in 1982 and graduated cum laude from the Halvern Plains School of Law in 1986 with a J.D.

Industry/Entity Type

Lawyer

Number of Pages Required

4 page

Requirements
Must have
• Introduction to firm; separate biography of principal; representative cases; testemonials; blog; method of contact

```html
<!DOCTYPE html>
<html lang="en">
<head>
<meta charset="utf-8">
<title>The Marlow Law Firm</title>
<link href="https://fonts.googleapis.com/css2?family=Mulish:ital,wght@0,400;0,600;0,700;1,400&display=swap" rel="stylesheet">
<style>
:root{
  --gold:#e9a93c;
  --gold-bright:#f3b948;
  --ink:#333333;
  --text:#6d6d6d;
  --muted:#8a8a8a;
  --rule:#e2e2e2;
  --dark:#3a3a3a;
  --hero-a:#a9360a;
  --hero-b:#d0561c;
  --band-a:#f1b43e;
  --band-b:#f7c862;
  --band-text:#5b4318;
  --white:#ffffff;
}
*{box-sizing:border-box;margin:0;padding:0}
html,body{width:866px;height:1200px;overflow:hidden;background:var(--white)}
body{position:relative;font-family:'Mulish',sans-serif;color:var(--text)}
.abs{position:absolute}
.btn{position:absolute;background:#3c3c3c;color:var(--white);font-size:9px;display:flex;align-items:center;justify-content:center;border:1px solid #2a2a2a}

/* header */
.topline{left:0;top:0;width:866px;height:3px;background:var(--gold-bright)}
.brand{left:54px;top:20px;font-size:8px;font-weight:700;color:var(--ink);letter-spacing:.3px;display:flex;align-items:center;gap:5px}
.brand .mark{width:10px;height:10px;background:var(--gold)}
.nav{left:420px;top:46px;display:flex;font-size:10px;color:#444;letter-spacing:.2px}
.nav a{color:inherit;text-decoration:none;padding:8px 8px 0;margin-right:8px;border-top:3px solid transparent}
.nav a.active{border-top-color:#555}

/* hero */
.hero{left:0;top:76px;width:866px;height:276px;background:linear-gradient(90deg,var(--hero-a) 0%,var(--hero-b) 45%,#c8581f 70%,#8c3a1a 100%)}
.hero-title{left:53px;top:142px;font-size:31px;font-weight:700;color:var(--gold-bright);letter-spacing:.3px}
.hero-sub{left:53px;top:182px;font-size:23px;line-height:27px;color:var(--white);width:360px}
.hero .btn{left:53px;top:176px}
.hero-btn{left:53px;top:252px;width:100px;height:28px;font-size:11px;font-weight:600;background:#333}
.dots{left:53px;top:314px;display:flex;gap:4px}
.dots span{width:9px;height:9px;border-radius:50%;background:var(--white)}
.dots span:first-child{background:var(--gold-bright)}

/* welcome */
.team-photo{left:53px;top:377px;width:239px;height:156px;background:linear-gradient(180deg,#3a3a3a,#1c1c1c)}
.h2{font-size:18px;color:var(--gold);font-weight:400}
.welcome-title{left:314px;top:374px}
.welcome-text{left:313px;top:402px;width:492px;font-size:8.8px;line-height:15.3px}
.welcome-btn{left:313px;top:509px;width:72px;height:24px}

/* principal band */
.band{left:0;top:556px}
.principal-title{left:53px;top:596px;color:var(--white)}
.principal-text{left:53px;top:624px;width:480px;font-size:8.8px;line-height:15.3px;color:var(--band-text)}
.checks{font-size:8.8px;color:var(--band-text);list-style:none}
.checks li{height:17.4px;display:flex;align-items:center;gap:6px}
.checks svg{flex:none}
.checks-a{left:53px;top:659px}
.checks-b{left:327px;top:659px}
.principal-btn{left:53px;top:762px;width:72px;height:24px}
.principal-photo{left:575px;top:600px;width:239px;height:156px;background:radial-gradient(circle at 50% 45%,#6a6a6a 0%,#262626 45%,#050505 80%)}

/* three columns */
.col-title{top:820px}
.col-rule{top:822px;width:1px;height:220px;background:var(--rule)}
.item{position:absolute;width:219px;border-bottom:1px solid var(--rule);padding-bottom:5px}
.item:last-of-type{border-bottom:none}
.item h3{font-size:10.4px;font-weight:600;color:var(--ink);margin-bottom:3px}
.item p{font-size:8.6px;line-height:13.3px;color:var(--text)}
.item .date{font-style:italic;color:var(--gold);font-size:8.2px}
.testi{position:absolute;left:313px;width:240px;height:66px;display:flex;gap:11px}
.testi .avatar{width:44px;height:44px;background:linear-gradient(160deg,#9b8a7a,#4a4a52);flex:none}
.testi h3{font-size:10.4px;font-weight:600;color:var(--ink);margin:-1px 0 2px}
.testi p{font-size:8.6px;line-height:13.3px;font-style:italic;color:var(--muted)}
.testi-body{border-bottom:1px solid var(--rule);width:163px;padding-bottom:6px}
.cases-btn{left:53px;top:1017px;width:72px;height:24px}

/* footer */
.footer{left:0;top:1060px}
.f-title{font-size:11px;color:var(--gold);font-weight:600}
.f-col{position:absolute;top:1084px;font-size:8.6px;color:#e6e6e6;line-height:17.4px}
.f-col a{display:block;color:inherit;text-decoration:none}
.f-contact{left:200px;top:1084px;line-height:14.6px}
.f-contact strong{font-weight:600;font-size:10px;display:block;margin-bottom:1px}
.f-contact .hl{color:var(--gold)}
.social{left:383px;top:1108px;display:flex;gap:7px}
.social span{width:20px;height:20px;border-radius:50%;background:var(--gold)}
.f-brand{left:671px;top:1098px;font-size:7px;font-weight:700;color:var(--white);letter-spacing:.3px;display:flex;align-items:center;gap:4px}
.f-brand .mark{width:8px;height:8px;background:var(--white)}
.copy{left:671px;top:1148px;font-size:8.4px;line-height:13px;color:#bdbdbd}
</style>
</head>
<body>

<header>
  <div class="abs topline"></div>
  <div class="abs brand"><span class="mark"></span>THE MARLOW LAW FIRM</div>
  <nav class="abs nav">
    <a class="active" href="#">HOME</a><a href="#">WHO WE ARE</a><a href="#">PRACTICE AREAS</a><a href="#">RESOURCES</a><a href="#">CONTACT US</a>
  </nav>
</header>

<section>
  <div class="abs hero" role="img" aria-label="Photo of chess pieces on a board with a fallen white king, against an orange backdrop"></div>
  <h1 class="abs hero-title">THE MARLOW LAW FIRM</h1>
  <p class="abs hero-sub">We specialize in serious auto and trucking accidents.</p>
  <a class="btn hero-btn">CONTACT US</a>
  <div class="abs dots"><span></span><span></span><span></span><span></span></div>
</section>

<section>
  <div class="abs team-photo" role="img" aria-label="Group photo of the firm's team in dark suits"></div>
  <h2 class="abs h2 welcome-title">Welcome to Our Website</h2>
  <p class="abs welcome-text">Aliquam molestie, mi et imperdiet euismod, dui purus auctor tellus, et interdum lacus lectus et ante. Sed accumsan sollicitudin sapien, sit amet adipiscing turpis gravida ac. In congue, neque ac lobortis volutpat, libero mauris varius mi, vitae suscipit ipsum ligula vitae risus. Duis aliquam nibh a dui iaculis viverra id a velit. Vivamus egestas risus in magna varius commodo. Sed semper viverra egestas. Etiam pretium porttitor lectus, vel ornare neque porta volutpat. Aenean a nibh eget turpis vehicula tempus ac sed massa. Vestibulum dolor nulla, ultrices ac tincidunt sed, laoreet non est. Suspendisse lobortis turpis in odio blandit ac interdum lorem euismod.</p>
  <a class="btn welcome-btn">Read More</a>
</section>

<section>
  <svg class="abs band" width="866" height="250" role="img" aria-label="Golden toned photo of law book spines">
    <defs><linearGradient id="bandGrad" x1="0" x2="1"><stop offset="0" stop-color="#f1b43e"/><stop offset=".55" stop-color="#f6c65e"/><stop offset="1" stop-color="#f0b23c"/></linearGradient></defs>
    <polygon points="0,18 866,0 866,240 0,248" fill="url(#bandGrad)"/>
  </svg>
  <h2 class="abs h2 principal-title">Our Principal</h2>
  <p class="abs principal-text">Aliquam molestie, mi et imperdiet euismod, dui purus auctor tellus, et interdum lacus lectus et ante. Sed accumsan sollicitudin sapien, sit amet adipiscing turpis gravida ac..</p>
  <ul class="abs checks checks-a">
    <li><svg width="8" height="8" viewBox="0 0 8 8"><path d="M1 4.2 3 6.2 7 1.6" fill="none" stroke="#3a2a10" stroke-width="1.6"/></svg>Duis aliquam nibh a dui iaculis viverra id a velit</li>
    <li><svg width="8" height="8" viewBox="0 0 8 8"><path d="M1 4.2 3 6.2 7 1.6" fill="none" stroke="#3a2a10" stroke-width="1.6"/></svg>Vivamus egestas risus in magna varius commodo</li>
    <li><svg width="8" height="8" viewBox="0 0 8 8"><path d="M1 4.2 3 6.2 7 1.6" fill="none" stroke="#3a2a10" stroke-width="1.6"/></svg>Sed semper viverra egestas</li>
    <li><svg width="8" height="8" viewBox="0 0 8 8"><path d="M1 4.2 3 6.2 7 1.6" fill="none" stroke="#3a2a10" stroke-width="1.6"/></svg>Etiam pretium porttitor lectus</li>
    <li><svg width="8" height="8" viewBox="0 0 8 8"><path d="M1 4.2 3 6.2 7 1.6" fill="none" stroke="#3a2a10" stroke-width="1.6"/></svg>Aenean a nibh eget turpis vehicula tempus ac sed massa</li>
  </ul>
  <ul class="abs checks checks-b">
    <li><svg width="8" height="8" viewBox="0 0 8 8"><path d="M1 4.2 3 6.2 7 1.6" fill="none" stroke="#3a2a10" stroke-width="1.6"/></svg>Vivamus egestas risus in magna varius commodo</li>
    <li><svg width="8" height="8" viewBox="0 0 8 8"><path d="M1 4.2 3 6.2 7 1.6" fill="none" stroke="#3a2a10" stroke-width="1.6"/></svg>Sed semper viverra egestas</li>
    <li><svg width="8" height="8" viewBox="0 0 8 8"><path d="M1 4.2 3 6.2 7 1.6" fill="none" stroke="#3a2a10" stroke-width="1.6"/></svg>Etiam pretium porttitor lectus</li>
  </ul>
  <a class="btn principal-btn">Read More</a>
  <div class="abs principal-photo" role="img" aria-label="Black and white portrait of the principal attorney in a tuxedo"></div>
</section>

<section>
  <h2 class="abs h2 col-title" style="left:52px">Representative Cases</h2>
  <div class="item" style="left:53px;top:852px"><h3>Business Law</h3><p>Aliquam molestie, mi et imperdiet euismod, dui purus auctor tellus, et interdum lacus lectus et ante</p></div>
  <div class="item" style="left:53px;top:904px"><h3>Civil Litigation</h3><p>Aliquam molestie, mi et imperdiet euismod, dui purus auctor tellus, et interdum lacus lectus et ante</p></div>
  <div class="item" style="left:53px;top:956px;border-bottom:none"><h3>Criminal Defense</h3><p>Aliquam molestie, mi et imperdiet euismod, dui purus auctor tellus, et interdum lacus lectus et ante</p></div>
  <a class="btn cases-btn">Read More</a>

  <div class="abs col-rule" style="left:293px"></div>

  <h2 class="abs h2 col-title" style="left:313px">Testimonials</h2>
  <div class="testi" style="top:854px"><div class="avatar" role="img" aria-label="Client portrait"></div><div class="testi-body"><h3>Name goes here</h3><p>“Aliquam molestie, mi et imperdiet euismod, dui purus auctor tellus, et interdum lacus lectus et ante...”</p></div></div>
  <div class="testi" style="top:922px"><div class="avatar" role="img" aria-label="Client portrait"></div><div class="testi-body"><h3>Name goes here</h3><p>“Aliquam molestie, mi et imperdiet euismod, dui purus auctor tellus, et interdum lacus lectus et ante...”</p></div></div>
  <div class="testi" style="top:990px"><div class="avatar" role="img" aria-label="Client portrait"></div><div class="testi-body" style="border-bottom:none"><h3>Name goes here</h3><p>“Aliquam molestie, mi et imperdiet euismod, dui purus auctor tellus, et interdum lacus lectus et ante...”</p></div></div>

  <div class="abs col-rule" style="left:560px"></div>

  <h2 class="abs h2 col-title" style="left:575px">Blog Posts</h2>
  <div class="item" style="left:575px;top:852px;width:217px"><h3>Ultricies et sollicitudin pretium...</h3><p>Aliquam molestie, mi et imperdiet euismod, dui purus auctor tellus, et interdum lacus lectus et ante.</p><p class="date">Posted on 2 days ago</p></div>
  <div class="item" style="left:575px;top:920px;width:217px"><h3>Ultricies et sollicitudin pretium...</h3><p>Aliquam molestie, mi et imperdiet euismod, dui purus auctor tellus, et interdum lacus lectus et ante.</p><p class="date">Posted on 2 days ago</p></div>
  <div class="item" style="left:575px;top:988px;width:217px;border-bottom:none"><h3>Ultricies et sollicitudin pretium...</h3><p>Aliquam molestie, mi et imperdiet euismod, dui purus auctor tellus, et interdum lacus lectus et ante.</p><p class="date">Posted on 2 days ago</p></div>
</section>

<footer>
  <svg class="abs footer" width="866" height="140"><polygon points="0,0 866,12 866,140 0,140" fill="#3a3a3a"/></svg>
  <h4 class="abs f-title" style="left:64px;top:1085px">Company</h4>
  <nav class="f-col" style="left:64px;top:1101px">
    <a href="#">Home</a><a href="#">Who We Are</a><a href="#">Practice Areas</a><a href="#">Resources</a><a href="#">Contact Us</a>
  </nav>
  <h4 class="abs f-title" style="left:200px;top:1085px">Contact Info</h4>
  <div class="f-col f-contact" style="top:1102px">
    <strong>MarlowLawFirm</strong>
    42 Harlan Row Brenton,<br>GA 31599<br>
    Phone: <span class="hl">555.014.2290</span><br>
    Email: <span class="hl">info@marlowlawfirm.com</span>
  </div>
  <h4 class="abs f-title" style="left:383px;top:1085px">Connect Us</h4>
  <div class="abs social"><span></span><span></span><span></span><span></span></div>
  <div class="abs f-brand"><span class="mark"></span>THE MARLOW LAW FIRM</div>
  <p class="abs copy">Copyright © 2014. Company Name.<br>All Right Reserved</p>
</footer>

</body>
</html>
```